Kelvane Plumbing Business cards

Company is Kelvane Plumbing.
name Dashel Morrowby, I am a plumber, drainer, gasfitter and roofer
Mobile: 0431 906 154
Email address: info@kelvaneplumbing.example (check out my website for some ideas)
Website: www.kelvaneplumbing.example
ABN: 82 916 203 471
LIC: 604517K

I am reliable all round plumber. I am a 24 hour emergency service. Kelvane Plumbing is a professional plumbing service in the Illawarra, South Coast, Southern Sydney and Southern Highland regions of NSW. We offer a 24 hour emergency service for piece of mind to our customers. Call us now to see how we can help you. Kelvane Plumbing approaches every job with attention to detail and excellent customer service. With our superior workmanship you can be confident that the job will be done right the first time around. You can rest assured with results that are guaranteed to last.

Target Market(s)

the general public

Contact Information for Business Card

look up website for some ideas something with similar colours to logo and new modern and to catch the eye.

Colors
fdfdfd
ffffff
000000
7f7f7f
aaaaaa
33a6d7
0492cd

Requirements
Must have
• all contact details
• company- Kelvane Plumbing
• name- Dashel Morrowby
• number mobile- 0431 906 154
• Email address- info@kelvaneplumbing.example
• Website- www.kelvaneplumbing.example
• ABN- 82 916 203 471
• LIC- 604517K

```html
<!DOCTYPE html>
<html lang="en">
<head>
<meta charset="utf-8">
<title>Kelvane Plumbing – Business Cards</title>
<link rel="stylesheet" href="https://fonts.googleapis.com/css2?family=Montserrat:wght@400;500;600;700&display=swap">
<style>
  :root {
    --stage: #2a2a2b;
    --card: #1b1b1c;
    --white: #fdfdfd;
    --grey: #7f7f7f;
    --grey-light: #aaaaaa;
    --blue: #0492cd;
    --blue-light: #33a6d7;
    --deco: #2c2c2e;
  }
  * { box-sizing: border-box; margin: 0; padding: 0; }
  html, body { width: 1200px; height: 895px; overflow: hidden; background: var(--stage); }
  body { font-family: "Montserrat", Arial, sans-serif; color: var(--white); position: relative; }

  .card {
    position: absolute; left: 300px; width: 600px; height: 343px;
    background: var(--card); border-radius: 16px; overflow: hidden;
    border-bottom: 7px solid var(--blue);
    box-shadow: 0 18px 40px rgba(0,0,0,.45);
  }
  .card--front { top: 64px; }
  .card--back { top: 470px; }

  /* front */
  .front__brand {
    position: absolute; top: 92px; left: 0; right: 0; text-align: center;
    font-weight: 600; font-size: 44px; letter-spacing: 2px; color: var(--grey-light);
    text-transform: uppercase;
  }
  .front__region-label {
    position: absolute; top: 200px; left: 60px; right: 60px;
    display: flex; align-items: center; gap: 14px;
    color: var(--blue); font-weight: 700; font-size: 20px;
  }
  .front__region-label .rule { flex: 1; height: 1px; background: var(--white); }
  .front__regions {
    position: absolute; top: 238px; left: 0; right: 0; text-align: center;
    font-size: 16px; font-weight: 400; color: var(--white);
  }

  /* back */
  .back__brand {
    position: absolute; top: 38px; right: 34px;
    display: flex; align-items: center; gap: 10px;
    font-weight: 600; font-size: 22px; color: var(--blue); text-transform: uppercase;
  }
  .back__brand-dot { width: 16px; height: 16px; border-radius: 50%; background: var(--blue); }
  .back__deco {
    position: absolute; left: 70px; top: 90px; width: 170px; height: 170px;
    border-radius: 12px; background: radial-gradient(circle, #333336 0%, var(--card) 75%);
  }
  .back__identity { position: absolute; right: 34px; top: 130px; text-align: right; }
  .back__name { font-weight: 700; font-size: 30px; color: var(--blue); }
  .back__rule-row { display: flex; align-items: center; gap: 10px; margin-top: 4px; }
  .back__rule-row .rule { width: 120px; height: 1px; background: var(--white); }
  .back__trades { font-size: 15px; }
  .back__ids { margin-top: 8px; font-size: 15px; line-height: 1.4; }
  .back__ids .label { color: var(--blue); }

  .back__contact {
    position: absolute; left: 40px; bottom: 26px; width: 360px;
    border-top: 1px solid var(--white); padding-top: 12px;
    font-size: 15px; line-height: 1.55;
  }
  .contact__row { display: flex; align-items: center; gap: 10px; }
  .contact__row svg { width: 14px; height: 14px; flex: none; fill: var(--blue); }
  .contact__row .accent { color: var(--blue-light); }
</style>
</head>
<body>

<section class="card card--front">
  <div class="front__brand">Kelvane Plumbing</div>
  <div class="front__region-label"><span class="rule"></span>NSW<span class="rule"></span></div>
  <div class="front__regions">Illawarra | South Coast | Southern Sydney | Southern Highland</div>
</section>

<section class="card card--back">
  <div class="back__brand"><span class="back__brand-dot"></span>Kelvane Plumbing</div>
  <div class="back__deco" role="img" aria-label="Faint crossed wrench and pipe decoration"></div>

  <div class="back__identity">
    <div class="back__name">Dashel Morrowby</div>
    <div class="back__rule-row"><span class="rule"></span><span class="back__trades">Plumber | Drainer | Gasfitter | Roofer</span></div>
    <div class="back__ids">
      <div><span class="label">ABN:</span> 82 916 203 471</div>
      <div><span class="label">LIC:</span> 604517K</div>
    </div>
  </div>

  <div class="back__contact">
    <div class="contact__row">
      <svg viewBox="0 0 16 16" aria-hidden="true"><path d="M3.6 1.5l2.3 2.6-1.3 1.7c.9 2 2.6 3.7 4.6 4.6l1.7-1.3 2.6 2.3-1.3 2.1C7 13.3 2.7 9 1.5 3.4z"/></svg>
      <span>0431 906 154</span>
    </div>
    <div class="contact__row">
      <svg viewBox="0 0 16 16" aria-hidden="true"><path d="M1 3h14v10H1z M2 4l6 5 6-5" fill="var(--blue)" stroke="var(--card)" stroke-width="1"/></svg>
      <span>info@<span class="accent">kelvaneplumbing</span>.example</span>
    </div>
    <div class="contact__row">
      <svg viewBox="0 0 16 16" aria-hidden="true"><circle cx="8" cy="8" r="7"/><path d="M1 8h14M8 1c-3 3-3 11 0 14M8 1c3 3 3 11 0 14" fill="none" stroke="var(--card)" stroke-width="1"/></svg>
      <span>www.<span class="accent">kelvaneplumbing</span>.example</span>
    </div>
  </div>
</section>

</body>
</html>
```